Surface Protection company needs cards

We are a New Zealand company that will apply nanotechnology coatings on surfaces to prevent growth and spread of bacteria, viruses, mold etc with a sprayer. We deal with large corporates, airlines, hospitals and schools so we are after a new modern, simple and clean look that will have great visual impact.
We a company that is focused on prevention and protection.

Company name, Vela Shield

Subtext, Antimicrobial Surface Protection

Logo, VS

Target Market(s)

Hospitals, Transport agencies, Airlines, Corporate entities

Contact Information for Business Card

Company name, VelaShield
Logo, VS

Gareth Tolley
velashieldnz@postbox.example
+64219305562
www.velashield.example.nz

Requirements
Must have
• Simple clean look.
Nice to have
• We apply nano coatings so try and incorporate this into a theme somehow

```html
<!DOCTYPE html>
<html lang="en">
<head>
<meta charset="utf-8">
<title>Vela Shield – Business Cards</title>
<link rel="stylesheet" href="https://fonts.googleapis.com/css2?family=Raleway:wght@400;500;800&family=Open+Sans:wght@400;600&display=swap">
<style>
  :root {
    --blue: #0aa7e9;
    --green: #62ae43;
    --ink: #333333;
    --muted: #8d9196;
    --paper: #ffffff;
    --stage: #383838;
    --sparkle-zone: #f1f2f3;
  }
  * { box-sizing: border-box; margin: 0; padding: 0; }
  html, body { width: 717px; height: 1200px; overflow: hidden; }
  body { background: var(--stage); position: relative; }

  .card {
    position: absolute;
    left: 48px;
    width: 620px;
    height: 354px;
    background: var(--paper);
    overflow: hidden;
  }
  .card--front { top: 206px; }
  .card--back { top: 640px; }

  /* front */
  .sparkle-zone {
    position: absolute;
    left: 39px; top: 22px;
    width: 121px; height: 126px;
    border-radius: 10px;
    background: radial-gradient(circle at 55% 60%, #eceef0, var(--sparkle-zone) 70%, transparent);
  }
  .tagline {
    position: absolute;
    right: 31px; top: 36px;
    text-align: right;
    font-family: "Raleway", sans-serif;
    font-weight: 800;
    font-size: 30px;
    line-height: 35px;
    color: var(--blue);
    letter-spacing: 0.2px;
  }
  .person {
    position: absolute;
    right: 31px; top: 148px;
    text-align: right;
  }
  .person__name {
    font-family: "Raleway", sans-serif;
    font-weight: 800;
    font-size: 20px;
    line-height: 23px;
    color: var(--ink);
  }
  .person__role {
    display: inline-block;
    font-family: "Raleway", sans-serif;
    font-weight: 400;
    font-size: 16px;
    line-height: 20px;
    color: var(--ink);
    padding-bottom: 2px;
    border-bottom: 1.5px solid var(--blue);
  }
  .contacts {
    position: absolute;
    right: 31px; top: 216px;
    list-style: none;
  }
  .contacts li {
    display: flex;
    justify-content: flex-end;
    align-items: center;
    gap: 12px;
    height: 29.5px;
    font-family: "Open Sans", sans-serif;
    font-size: 13.5px;
    color: var(--ink);
  }
  .contacts svg { width: 18px; height: 18px; flex: none; }

  .brand {
    display: flex;
    align-items: center;
    gap: 10px;
    font-family: "Raleway", sans-serif;
    font-weight: 800;
    color: var(--blue);
    white-space: nowrap;
  }
  .brand__dot { border-radius: 50%; background: var(--blue); flex: none; }
  .brand--front { position: absolute; left: 30px; top: 252px; font-size: 29px; }
  .brand--front .brand__dot { width: 20px; height: 20px; }

  .band { position: absolute; left: 0; bottom: 0; width: 620px; height: 25px; }

  /* back */
  .side-tab { position: absolute; top: 0; width: 20px; height: 354px; }
  .side-tab--left { left: 0; }
  .side-tab--right { right: 0; }
  .back-lockup {
    position: absolute;
    left: 0; right: 0; top: 148px;
    display: flex; flex-direction: column; align-items: center;
  }
  .brand--back { font-size: 36px; gap: 12px; }
  .brand--back .brand__dot { width: 24px; height: 24px; }
  .back-lockup__sub {
    margin-top: 8px;
    font-family: "Raleway", sans-serif;
    font-weight: 500;
    font-size: 12px;
    letter-spacing: 1.3px;
    color: var(--muted);
  }
  .back-url {
    position: absolute;
    left: 0; right: 0; top: 308px;
    text-align: center;
    font-family: "Raleway", sans-serif;
    font-size: 16px;
    color: var(--ink);
  }
</style>
</head>
<body>

<section class="card card--front" aria-label="Business card front">
  <div class="sparkle-zone" role="img" aria-label="Faint grey sparkle decoration"></div>

  <h1 class="tagline">ANTIMICROBIAL<br>SURFACE PROTECTION</h1>

  <div class="person">
    <p class="person__name">GARETH TOLLEY</p>
    <p class="person__role">Solution Manager</p>
  </div>

  <ul class="contacts">
    <li>+64219305562
      <svg viewBox="0 0 18 18" aria-hidden="true"><rect width="18" height="18" rx="3" fill="var(--blue)"/><path d="M5.6 4.2l1.8-.3 1 2.4-1.2.9c.6 1.4 1.6 2.4 3 3l.9-1.2 2.4 1-.3 1.8c-4.3.3-7.9-3.3-7.6-7.6z" fill="#fff"/></svg>
    </li>
    <li>velashieldnz@postbox.example
      <svg viewBox="0 0 18 18" aria-hidden="true"><rect width="18" height="18" rx="3" fill="var(--blue)"/><rect x="4" y="5.5" width="10" height="7" fill="none" stroke="#fff" stroke-width="1.3"/><path d="M4 5.5l5 4 5-4" fill="none" stroke="#fff" stroke-width="1.3"/></svg>
    </li>
    <li>www.velashield.example.nz
      <svg viewBox="0 0 18 18" aria-hidden="true"><rect width="18" height="18" rx="3" fill="var(--blue)"/><circle cx="9" cy="9" r="5" fill="none" stroke="#fff" stroke-width="1.3"/><ellipse cx="9" cy="9" rx="2" ry="5" fill="none" stroke="#fff" stroke-width="1"/><path d="M4 9h10" stroke="#fff" stroke-width="1"/></svg>
    </li>
  </ul>

  <div class="brand brand--front"><span class="brand__dot"></span>VELA SHIELD</div>

  <svg class="band" viewBox="0 0 620 25" aria-hidden="true">
    <polygon points="0,0 324,0 300,25 0,25" fill="var(--green)"/>
    <polygon points="337,0 620,0 620,25 313,25" fill="var(--blue)"/>
  </svg>
</section>

<section class="card card--back" aria-label="Business card back">
  <svg class="side-tab side-tab--left" viewBox="0 0 20 354" aria-hidden="true">
    <polygon points="0,75 19,87 19,247 0,259" fill="var(--blue)"/>
  </svg>
  <svg class="side-tab side-tab--right" viewBox="0 0 20 354" aria-hidden="true">
    <polygon points="20,75 1,87 1,247 20,259" fill="var(--blue)"/>
  </svg>

  <div class="back-lockup">
    <div class="brand brand--back"><span class="brand__dot"></span>VELA SHIELD</div>
    <p class="back-lockup__sub">ANTIMICROBIAL SURFACE PROTECTION</p>
  </div>

  <p class="back-url">www.velashield.example.nz</p>
</section>

</body>
</html>
```